Dorvan-Klamp: What Sets Us Apart

My client wants a brochure design (8.5 x 11 folds to 5.5 x 8.5) for their orthodontia practice. Attached is what they currently produce in-house. In my client's request to me: "We want to change this document into a bi-fold brochure that is colorful and attractive and easy to read…bigger, more colorful font, colored paper? We also want to add our contact information. We are completely open to your artistic ideas on how to do this. Let me know your thoughts. Patients/parents take this home with them if they leave our office “uncommitted” to starting treatment and state they will call us back. It needs to be the tool that we hope will help them choose us and call back to schedule." I really do not want 50 designs back. I might want to look at 3 or 5, unless those all are just plain ugly. The text my client wants is attached. I can upload two other pieces they currently use and their logo if I choose to move forward.

```html
<!DOCTYPE html>
<html lang="en">
<head>
<meta charset="utf-8">
<title>Dorvan-Klamp Orthodontics – What Sets Us Apart</title>
<link href="https://fonts.googleapis.com/css2?family=Open+Sans:wght@400;600;700;800&display=swap" rel="stylesheet">
<style>
  :root {
    --page-bg: #e9e9e9;
    --paper: #ffffff;
    --ink: #2b2b2b;
    --body-text: #6a6a6a;
    --green: #8cc63f;
    --green-dark: #6fa52b;
    --black: #1d1d1d;
    --grey-light: #ececec;
    --grey-mid: #d2d2d2;
    --dot-warm: rgba(201, 122, 44, .22);
    --dot-brown: rgba(122, 75, 37, .16);
    --dot-grey: rgba(170, 170, 170, .18);
  }
  * { box-sizing: border-box; margin: 0; padding: 0; }
  html, body { width: 800px; height: 1200px; overflow: hidden; }
  body { background: var(--page-bg); font-family: "Open Sans", Arial, sans-serif; color: var(--ink); position: relative; }

  .spread { position: absolute; left: 20px; width: 760px; background: var(--paper); overflow: hidden; box-shadow: 0 2px 6px rgba(0,0,0,.12); }
  .spread--outside { top: 20px; height: 570px; }
  .spread--inside { top: 610px; height: 570px; }
  .spread__art { position: absolute; inset: 0; width: 100%; height: 100%; }

  .fold { position: absolute; top: 0; bottom: 0; left: 380px; width: 1px; background: rgba(0,0,0,.06); }

  /* decorative dot-pattern areas, shown as soft tonal fields */
  .dot-field { position: absolute; border-radius: 40px; }
  .dot-field--back { left: 62px; top: 18px; width: 190px; height: 180px;
    background: radial-gradient(ellipse at 40% 40%, var(--dot-warm) 0%, var(--dot-brown) 40%, var(--dot-grey) 65%, rgba(255,255,255,0) 80%); }
  .dot-field--cover { left: 440px; top: 14px; width: 100px; height: 260px;
    background: radial-gradient(ellipse at 50% 45%, var(--dot-warm) 0%, var(--dot-brown) 40%, var(--dot-grey) 65%, rgba(255,255,255,0) 82%); }
  .dot-field--inside { left: 20px; top: 14px; width: 720px; height: 95px;
    background: radial-gradient(ellipse at 50% 50%, var(--dot-warm) 0%, var(--dot-brown) 35%, var(--dot-grey) 60%, rgba(255,255,255,0) 78%); }

  /* brand strip */
  .brand-strip { position: absolute; background: var(--black); display: flex; align-items: center; justify-content: center; }
  .brand-strip__name { color: #fff; font-weight: 700; font-size: 13px; letter-spacing: 3px; text-transform: uppercase; white-space: nowrap; }
  .brand-strip--vertical .brand-strip__name { transform: rotate(-90deg); }
  .brand-strip--top { left: 14px; top: 0; width: 34px; height: 150px; }
  .brand-strip--bottom { left: 14px; top: 360px; width: 34px; height: 150px; }
  .brand-strip--cover { left: 400px; top: 0; width: 34px; height: 150px; }

  /* back panel contact */
  .contact { position: absolute; left: 120px; top: 400px; width: 250px; text-align: right; }
  .contact__title { color: var(--green); font-weight: 700; font-size: 20px; margin-bottom: 6px; }
  .contact__line { font-size: 11px; font-weight: 600; color: var(--ink); line-height: 1.6; white-space: nowrap; }

  /* cover */
  .cover-photo { position: absolute; left: 520px; top: 50px; width: 190px; height: 190px; border-radius: 50%;
    background: radial-gradient(circle at 55% 45%, #f3d2c4 0%, #d79a88 45%, #8e4a3f 75%, #3e2420 100%); }
  .cover-title { position: absolute; left: 420px; top: 290px; width: 330px; }
  .cover-title__heading { font-weight: 800; font-size: 34px; color: var(--ink); letter-spacing: -0.5px; line-height: 1.1; white-space: nowrap; }
  .cover-title__sub { color: var(--green-dark); font-weight: 600; font-size: 12.5px; margin-top: 6px; white-space: nowrap; }
  .cover-badge { position: absolute; left: 680px; top: 425px; width: 58px; height: 58px; border-radius: 50%; background: #3a3a3a; border: 3px solid var(--paper); box-shadow: 0 0 0 2px #3a3a3a; }
  .cover-call { position: absolute; left: 380px; right: 0; bottom: 0; height: 62px; background: #2f2f2f; display: flex; align-items: center; justify-content: flex-end; padding-right: 26px; }
  .cover-call__text { color: var(--green); font-weight: 800; font-size: 20px; letter-spacing: .5px; }

  /* inside */
  .features { position: absolute; top: 120px; width: 330px; }
  .features--left { left: 25px; }
  .features--right { left: 405px; }
  .feature { margin-bottom: 11px; }
  .feature__title { color: var(--green-dark); font-weight: 700; font-size: 11.5px; text-transform: uppercase; letter-spacing: .3px; margin-bottom: 3px; }
  .feature__text { font-size: 8.6px; line-height: 1.42; color: var(--body-text); }
</style>
</head>
<body>

<section class="spread spread--outside" aria-label="Brochure outside">
  <svg class="spread__art" viewBox="0 0 760 570" aria-hidden="true">
    <polygon points="60,0 380,0 380,250" fill="var(--grey-light)"/>
    <polygon points="200,0 380,0 380,140" fill="var(--grey-mid)"/>
    <polygon points="0,570 0,420 240,570" fill="var(--grey-light)"/>
    <polygon points="380,570 380,330 640,570" fill="var(--grey-light)"/>
    <polygon points="380,570 380,430 530,570" fill="var(--grey-mid)"/>
    <polygon points="760,0 620,0 760,140" fill="var(--grey-light)"/>
  </svg>
  <div class="fold"></div>

  <div class="dot-field dot-field--back" role="img" aria-label="Decorative pattern of scattered brown, orange and grey dots"></div>

  <div class="brand-strip brand-strip--vertical brand-strip--top"><span class="brand-strip__name">Dorvan-Klamp</span></div>
  <div class="brand-strip brand-strip--vertical brand-strip--bottom"><span class="brand-strip__name">Dorvan-Klamp</span></div>

  <div class="contact">
    <h2 class="contact__title">Contact Us</h2>
    <p class="contact__line">2840 Orchard Ln. | Milford, OH 44102</p>
    <p class="contact__line">(330) 555-0148</p>
    <p class="contact__line">www.dorvanklampsmiles.com</p>
  </div>

  <div class="brand-strip brand-strip--vertical brand-strip--cover"><span class="brand-strip__name">Dorvan-Klamp</span></div>
  <div class="dot-field dot-field--cover" role="img" aria-label="Decorative pattern of scattered brown, orange and grey dots"></div>
  <div class="cover-photo" role="img" aria-label="Photo of a smiling patient showing straight teeth"></div>
  <div class="cover-title">
    <h1 class="cover-title__heading">What Sets Us Apart</h1>
    <p class="cover-title__sub">Key traits to consider when choosing an orthodontist</p>
  </div>
  <div class="cover-badge" role="img" aria-label="Award badge"></div>
  <div class="cover-call"><span class="cover-call__text">CALL US: (330) 555-0148</span></div>
</section>

<section class="spread spread--inside" aria-label="Brochure inside">
  <svg class="spread__art" viewBox="0 0 760 570" aria-hidden="true">
    <polygon points="0,570 0,470 160,570" fill="var(--grey-light)"/>
    <polygon points="760,570 760,470 600,570" fill="var(--grey-light)"/>
  </svg>
  <div class="fold"></div>

  <div class="dot-field dot-field--inside" role="img" aria-label="Decorative band of scattered brown, orange and grey dots"></div>

  <div class="features features--left">
    <article class="feature"><h3 class="feature__title">Orthodontic Specialists</h3>
      <p class="feature__text">Consider the training behind your smile. Every orthodontist completes years of extra schooling after dental school, focused only on moving teeth and guiding jaw growth. Our doctors practice orthodontics exclusively, every single day.</p></article>
    <article class="feature"><h3 class="feature__title">Board Certified</h3>
      <p class="feature__text">Board certification is a voluntary step that only some orthodontists take. It requires written and clinical exams reviewed by peers, and renewal every ten years. Both of our doctors hold this credential and keep it current.</p></article>
    <article class="feature"><h3 class="feature__title">You Have Choices</h3>
      <p class="feature__text">Not every office that straightens teeth is run by a specialist. Take time to ask who will plan and monitor your care, and what training they have. A second opinion is always welcome here, with no pressure to decide.</p></article>
    <article class="feature"><h3 class="feature__title">Outstanding Online Reviews</h3>
      <p class="feature__text">Hear it from the families we treat. Hundreds of patients and parents have shared their experiences online, praising our friendly team, clear explanations and beautiful results. Read them before you choose.</p></article>
    <article class="feature"><h3 class="feature__title">Highly Trained, Experienced Staff with In House Lab</h3>
      <p class="feature__text">Our assistants are trained in-house and many have been with us for over a decade. Our on-site lab crafts retainers and appliances quickly, so repairs and replacements rarely mean a long wait.</p></article>
  </div>

  <div class="features features--right">
    <article class="feature"><h3 class="feature__title">State of the Art Technology</h3>
      <p class="feature__text">We invest in modern tools that make visits easier. Digital scans replace messy impressions, low-dose 3D imaging aids precise planning, and the latest wire systems help teeth move comfortably and efficiently.</p></article>
    <article class="feature"><h3 class="feature__title">Flexible Appointments</h3>
      <p class="feature__text">Busy schedules matter. We offer early morning and after-school visits, plus quick check-ins that keep time away from class and work short. Text reminders help you never miss an appointment.</p></article>
    <article class="feature"><h3 class="feature__title">Flexible Financial Plans</h3>
      <p class="feature__text">Treatment should fit your budget. We offer interest-free monthly payment plans, accept most insurance and file claims for you. Ask about our savings for families with more than one patient.</p></article>
    <article class="feature"><h3 class="feature__title">The Doctors' Doctor</h3>
      <p class="feature__text">Many local dentists and their own children choose our practice for treatment. When the professionals who know teeth best trust us with their families, you can feel confident doing the same.</p></article>
    <article class="feature"><h3 class="feature__title">On-Time Treatment</h3>
      <p class="feature__text">We plan each step carefully and track progress at every visit, so most patients finish on schedule. Our goal is a healthy, lasting smile in the shortest sensible time.</p></article>
    <article class="feature"><h3 class="feature__title">Top of the Line Materials</h3>
      <p class="feature__text">We use only proven brackets, wires and aligners from trusted makers. Quality materials break less often, feel more comfortable and deliver results that stay beautiful for years to come.</p></article>
  </div>
</section>

</body>
</html>
```